Private Investigation Business Card Design

I need a business card for a new private investigation company named Brisk Lens Inquiries. I perform mainly surveillance jobs, vehicle repossessions, document serves etc. The final design should aim for a professional look. The logo has a magnifying glass with stick man arms and legs and is in a running action to show the "BRISK" aspect of the name. If the colour scheme could remain the same as the website www.brisklensinquiries.example.au with silvers,blacks and a couple electric blue highlights.
Industry/Entity Type
Business
Contact Information for Business Card
Morgan Kilbride
Brisk Lens Inquiries
0438276104
PO Box 58, Fernvale NSW 2291
info@brisklensinquiries.example.au
www.brisklensinquiries.example.au
Look and feel
Each slider illustrates characteristics of the customer's brand and the style your logo design should communicate.

```html
<!DOCTYPE html>
<html lang="en">
<head>
<meta charset="utf-8">
<title>Brisk Lens Inquiries – Business Card</title>
<link rel="stylesheet" href="https://fonts.googleapis.com/css2?family=Montserrat:wght@500;600;800&display=swap">
<style>
  :root {
    --backdrop: #d8d4cd;
    --card: #e6e6e6;
    --electric-blue: #2f8ccf;
    --ink: #2b2b2b;
    --muted: #666666;
    --silver: #8a8d91;
    --ghost: #d6d6d6;
  }
  * { box-sizing: border-box; margin: 0; padding: 0; }
  html, body {
    width: 1200px; height: 1200px; overflow: hidden;
    background: var(--backdrop);
    font-family: "Montserrat", Arial, sans-serif;
  }
  .stage {
    position: relative; width: 1200px; height: 1200px;
    display: flex; flex-direction: column; align-items: center; justify-content: center; gap: 40px;
  }
  .card {
    position: relative; width: 520px; height: 320px;
    background: var(--card);
    box-shadow: 2px 3px 6px rgba(0,0,0,0.25);
    overflow: hidden;
  }
  .card-front { display: flex; align-items: center; justify-content: center; }
  .brand-lockup { display: flex; align-items: center; gap: 14px; }
  .brand-name {
    font-weight: 800; font-size: 30px; letter-spacing: 0.5px;
    color: var(--silver); text-transform: uppercase;
  }
  .brand-dot { width: 22px; height: 22px; border-radius: 50%; background: var(--silver); }

  .card-back .holder {
    position: absolute; left: 36px; top: 26px;
  }
  .holder-name {
    font-weight: 800; font-size: 22px; color: var(--electric-blue);
    text-transform: uppercase; letter-spacing: 0.2px;
  }
  .holder-company { font-weight: 600; font-size: 13px; color: var(--ink); margin-top: 2px; }
  .contact {
    position: absolute; left: 36px; font-weight: 500; font-size: 11px;
    color: var(--muted); line-height: 15px;
  }
  .contact-postal { top: 112px; }
  .contact-online { top: 176px; }
  .contact-online .label { color: var(--electric-blue); }
  .ghost-mark {
    position: absolute; left: 78px; top: 246px;
    width: 46px; height: 46px; border-radius: 50%;
    border: 2px solid var(--ghost);
  }
  .corner-brand {
    position: absolute; right: 24px; bottom: 22px;
    font-weight: 800; font-size: 11px; color: var(--silver);
    text-transform: uppercase; letter-spacing: 0.3px;
  }
</style>
</head>
<body>
  <main class="stage">
    <section class="card card-front" aria-label="Card front">
      <div class="brand-lockup">
        <span class="brand-name">Brisk Lens Inquiries</span>
        <span class="brand-dot" aria-hidden="true"></span>
      </div>
    </section>

    <section class="card card-back" aria-label="Card back">
      <div class="holder">
        <h1 class="holder-name">Morgan Kilbride</h1>
        <p class="holder-company">Brisk Lens Inquiries</p>
      </div>
      <p class="contact contact-postal">0438276104<br>PO Box 58, Fernvale NSW 2291</p>
      <p class="contact contact-online">
        <span class="label">E:</span> info@brisklensinquiries.example.au<br>
        <span class="label">W:</span> www.brisklensinquiries.example.au
      </p>
      <span class="ghost-mark" aria-hidden="true"></span>
      <span class="corner-brand">Brisk Lens Inquiries</span>
    </section>
  </main>
</body>
</html>
```